Business Card Design Project

I am a Chiropractor that is looking for a new business card.  Our logo was slightly changed lately, therefore need a new, more professional look.
We are a modern, non-stuffy chiropractic office.  Want a contemporary look that will let people know this is not your typical doctors office.  Our logo is red, and contains the name of our business: realign.  The u in the logo is green, stressing the most important part of our business: "u"

Target Market(s)
moderate to upper income bracket, family friendly
www.realignspine-example.com
Gordon Pell
Family Chiropractor
314 Hollis Rd
Larkdale, TX 78999
512.555.0147 phone
512.555.0148 fax
Industry/Entity Type
Business
Requirements
Must have
- www.realignspine-example.com
Gordon Pell
Family Chiropractor
314 Hollis Rd
Larkdale, TX 78999
512.555.0147 phone
512.555.0148 fax

```html
<!DOCTYPE html>
<html lang="en">
<head>
<meta charset="utf-8">
<title>Gordon Pell – Family Chiropractor</title>
<link rel="stylesheet" href="https://fonts.googleapis.com/css2?family=Roboto:wght@100;300&display=swap">
<style>
  :root {
    --panel-green: #70b340;
    --card-red: #ff4646;
    --ink-white: #ffffff;
  }
  html, body {
    margin: 0;
    padding: 0;
    width: 1200px;
    height: 600px;
    overflow: hidden;
    background: var(--card-red);
  }
  .card {
    position: relative;
    width: 1200px;
    height: 600px;
    background: var(--card-red);
    color: var(--ink-white);
    font-family: "Roboto", sans-serif;
    font-weight: 300;
    overflow: hidden;
  }
  .contact-panel {
    position: absolute;
    left: 0;
    top: 0;
    width: 408px;
    height: 600px;
    background: var(--panel-green);
    overflow: hidden;
  }
  .address {
    position: absolute;
    left: 15px;
    top: 138px;
    margin: 0;
    font-style: normal;
    font-size: 38px;
    line-height: 50px;
  }
  .contact-list {
    position: absolute;
    left: 0;
    top: 248px;
    margin: 0;
    display: grid;
    grid-template-columns: 84px auto;
    column-gap: 12px;
    row-gap: 0;
    align-items: baseline;
  }
  .contact-label {
    justify-self: end;
    font-size: 20px;
    margin: 0;
  }
  .contact-value {
    margin: 0;
    font-size: 38px;
    line-height: 50px;
    white-space: nowrap;
  }
  .contact-value.web {
    font-size: 24px;
    margin-left: 2px;
  }
  .identity {
    position: absolute;
    right: 16px;
    top: 196px;
    text-align: right;
  }
  .doctor-name {
    margin: 0;
    font-weight: 100;
    font-size: 86px;
    line-height: 100px;
    letter-spacing: 1px;
  }
  .doctor-title {
    margin: -2px 24px 0 0;
    font-weight: 300;
    font-size: 41px;
    line-height: 46px;
  }
</style>
</head>
<body>
  <main class="card">
    <section class="contact-panel">
      <address class="address">314 Hollis Rd<br>Larkdale, TX 78999</address>
      <dl class="contact-list">
        <dt class="contact-label">phone</dt>
        <dd class="contact-value">512-555-0147</dd>
        <dt class="contact-label">fax</dt>
        <dd class="contact-value">512-555-0148</dd>
        <dt class="contact-label">web</dt>
        <dd class="contact-value web">realignspine-example.com</dd>
      </dl>
    </section>
    <header class="identity">
      <h1 class="doctor-name">GORDON PELL</h1>
      <p class="doctor-title">Family Chiropractor</p>
    </header>
  </main>
</body>
</html>
```